Ad-Services Website

The project is for an agency which provides a 360 service around the world of printing and advertising. Without much focus on the advertising per say, but much more focus on the medium on which advertisement can be achieved, such as banners, moving banners, boards and so on.

Futhermore more the company deals with material printing so it has advertising agencies as clients.

Finally it represents several companies in Greece for materials around advertising such as stands, ad-walls, banners and so on.

The webpage needs to have web 2.0 look an feel, and it will lack in content, therefore the focus should not be in large sections of text.

I can have a pdf sent with a small presentation that was done to the client, and the structure to which he agreed to

The following website has the look & feel of what we are looking for

http://www.kolvara.gr

The companies current website where you can get the colors and logos from is

http://trumexsign.gr
Updates

Hello,

Thank you all very much for your designs, we really appreciate your contribution.

Maybe in our next project we can work together.

Best Regards,
Marek

Industry/Entity Type

Advertising

```html
<!DOCTYPE html>
<html lang="en">
<head>
<meta charset="utf-8">
<title>Meridian Advertising – Brands</title>
<link rel="stylesheet" href="https://fonts.googleapis.com/css2?family=Arimo:wght@400;700&family=Oswald:wght@500&display=swap">
<style>
  :root {
    --sage: #d2dbbe;
    --sage-dark: #97aa9a;
    --paper: #fafcf5;
    --slate: #3b5a6a;
    --footer: #3e5f6d;
    --footer-deep: #1f3441;
    --footer-link: #93a9ae;
    --text: #55605a;
    --icon: #5f7a80;
  }
  * { box-sizing: border-box; margin: 0; padding: 0; }
  html, body { width: 817px; height: 1200px; overflow: hidden; background: #ffffff; }
  body { font-family: "Arimo", Arial, sans-serif; color: var(--text); position: relative; }

  .page {
    position: absolute; left: 20px; top: 6px; width: 786px; height: 1190px;
    background: var(--paper); box-shadow: 0 0 4px rgba(0,0,0,.35); overflow: hidden;
  }

  /* Header */
  .site-header { position: absolute; left: 0; top: 0; width: 100%; height: 131px; background: var(--sage); border-bottom: 1px solid #b9c2a8; }
  .brand-name { position: absolute; left: 15px; top: 36px; font-size: 34px; font-weight: 700; color: #ffffff; letter-spacing: -0.5px; }
  .search { position: absolute; left: 581px; top: 20px; width: 162px; height: 25px; background: #fbfcf8; border: 1px solid #c3cbb3; font-size: 11px; color: #b8bdb2; padding: 6px 10px; }
  .search-icon { position: absolute; left: 749px; top: 18px; }

  .main-nav { position: absolute; left: 0; top: 0; width: 100%; height: 131px; }
  .nav-item { position: absolute; top: 68px; width: 120px; margin-left: -60px; text-align: center; }
  .nav-item svg { display: block; margin: 0 auto; }
  .nav-label { display: block; margin-top: 4px; font-family: "Oswald", "Arial Narrow", sans-serif; font-weight: 500; font-size: 15.5px; color: #2f4650; letter-spacing: .2px; }
  .nav-item.active::after { content: ""; position: absolute; left: 55px; top: 57px; border: 5px solid transparent; border-bottom-color: #9aa79c; border-top: 0; }

  /* Content */
  .page-title { position: absolute; left: 17px; top: 199px; font-size: 20px; font-weight: 700; color: var(--slate); }
  .intro { position: absolute; left: 15px; top: 248px; width: 757px; font-size: 10.6px; line-height: 20.4px; text-align: justify; }

  .brand-grid { position: absolute; left: 14px; top: 411px; width: 759px; display: grid; grid-template-columns: repeat(3, 245px); column-gap: 12px; row-gap: 47px; }
  .brand-card { height: 229px; background: var(--sage); box-shadow: 0 1px 3px rgba(0,0,0,.28); }
  .brand-card h2 { height: 16px; background: var(--sage-dark); color: #ffffff; font-weight: 400; font-size: 10.6px; line-height: 16px; padding-left: 6px; }
  .card-body { padding: 13px 13px 0 13px; }
  .card-top { display: flex; justify-content: space-between; }
  .brand-image { width: 113px; height: 97px; background: var(--paper); }
  .card-top p { width: 90px; font-size: 9px; line-height: 20.4px; text-align: justify; text-align-last: justify; margin-top: -3px; }
  .card-text { font-size: 9px; line-height: 20.4px; text-align: justify; margin-top: 4px; }

  /* Footer */
  .site-footer { position: absolute; left: 0; top: 1032px; width: 100%; height: 130px; background: var(--footer); }
  .footer-col { position: absolute; top: 16px; }
  .footer-col h3 { font-size: 10.6px; font-weight: 700; color: #ffffff; letter-spacing: .3px; margin-bottom: 11px; }
  .footer-col li { list-style: none; font-size: 9px; font-weight: 700; color: var(--footer-link); line-height: 20px; }
  .footer-bar { position: absolute; left: 0; top: 1162px; width: 100%; height: 28px; background: var(--footer-deep); font-size: 9px; font-weight: 700; color: #a9b7ba; text-align: center; line-height: 28px; }
  .social { position: absolute; right: 71px; top: 6px; display: flex; gap: 4px; }
  .social span { width: 17px; height: 17px; border-radius: 50%; background: #5f7a80; }
</style>
</head>
<body>
<div class="page">
  <header class="site-header">
    <div class="brand-name">meridian</div>
    <div class="search">Search</div>
    <svg class="search-icon" width="22" height="28" viewBox="0 0 22 28" aria-hidden="true">
      <circle cx="10" cy="10" r="7" fill="none" stroke="#5f7a80" stroke-width="4"/>
      <line x1="13" y1="16" x2="18" y2="25" stroke="#5f7a80" stroke-width="5" stroke-linecap="round"/>
    </svg>

    <nav class="main-nav">
      <div class="nav-item active" style="left:296px">
        <svg width="34" height="32" viewBox="0 0 34 32" aria-hidden="true">
          <g stroke="var(--icon)" stroke-width="1.6" fill="none">
            <line x1="17" y1="16" x2="6" y2="5"/><line x1="17" y1="16" x2="28" y2="5"/>
            <line x1="17" y1="16" x2="5" y2="20"/><line x1="17" y1="16" x2="29" y2="19"/>
            <line x1="17" y1="16" x2="10" y2="29"/><line x1="17" y1="16" x2="17" y2="3"/>
          </g>
          <g fill="#9fb3a8"><circle cx="6" cy="5" r="3"/><circle cx="28" cy="5" r="3"/><circle cx="17" cy="3" r="2.5"/><circle cx="5" cy="20" r="3"/><circle cx="29" cy="19" r="3"/><circle cx="10" cy="29" r="3"/></g>
          <circle cx="17" cy="16" r="3.5" fill="#fff" stroke="#2f4650" stroke-width="1.6"/>
        </svg>
        <span class="nav-label">BRANDS</span>
      </div>
      <div class="nav-item" style="left:399px">
        <svg width="34" height="32" viewBox="0 0 34 32" aria-hidden="true">
          <g fill="#7f9a93">
            <rect x="13" y="1" width="8" height="9"/><rect x="13" y="22" width="8" height="9"/>
            <rect x="2" y="12" width="9" height="8"/><rect x="23" y="12" width="9" height="8"/>
            <rect x="5" y="4" width="7" height="7" transform="rotate(45 8.5 7.5)"/><rect x="22" y="4" width="7" height="7" transform="rotate(45 25.5 7.5)"/>
            <rect x="5" y="21" width="7" height="7" transform="rotate(45 8.5 24.5)"/><rect x="22" y="21" width="7" height="7" transform="rotate(45 25.5 24.5)"/>
          </g>
          <circle cx="17" cy="16" r="5" fill="#a9bcb3"/>
        </svg>
        <span class="nav-label">PRINTING</span>
      </div>
      <div class="nav-item" style="left:508px">
        <svg width="34" height="32" viewBox="0 0 34 32" aria-hidden="true">
          <rect x="1" y="1" width="32" height="25" fill="#5f7a80"/>
          <polygon points="4,23 30,4 30,23" fill="#9fb3a8"/>
          <rect x="14" y="27" width="6" height="3" fill="#5f7a80"/>
        </svg>
        <span class="nav-label">DISPLAYS</span>
      </div>
      <div class="nav-item" style="left:628px">
        <svg width="46" height="32" viewBox="0 0 46 32" aria-hidden="true">
          <polygon points="10,12 36,3 36,28 10,20" fill="#7f9a93"/>
          <rect x="4" y="11" width="7" height="10" fill="#3f5963"/>
          <rect x="37" y="2" width="3" height="27" fill="#3f5963"/>
          <rect x="12" y="20" width="5" height="9" fill="#3f5963"/>
        </svg>
        <span class="nav-label">ADVERTISING</span>
      </div>
      <div class="nav-item" style="left:744px">
        <svg width="34" height="32" viewBox="0 0 34 32" aria-hidden="true">
          <circle cx="17" cy="16" r="16" fill="#5f7a80"/>
          <circle cx="17" cy="12" r="5.5" fill="#2f4650"/>
          <path d="M7 27 Q17 14 27 27 Z" fill="#2f4650"/>
        </svg>
        <span class="nav-label">ABOUT US</span>
      </div>
    </nav>
  </header>

  <h1 class="page-title">Brands »</h1>
  <p class="intro">Lorem ipsum dolor sit amet, consectetuer adipiscing elit, sed diam nonummy nibh euismod tincidunt ut laoreet dolore magna aliquam erat volutpat. Ut wisi enim ad minim veniam, quis nostrud exerci tation ullamcorper suscipit lobortis nisl ut aliquip ex ea commodo consequat. Duis autem vel eum iriure dolor in hendrerit in vulputate velit esse molestie consequat, vel illum dolore. Eu feugiat nulla facilisis at vero eros et accumsan et iusto odio dignissim qui blandit praesent luptatum zzril delenit augue duis dolore te feugait nulla facilisi. Nam liber tempor cum soluta nobis eleifend option congue nihil imperdiet doming id quod mazim placerat facer possim assum. Typi non habent claritatem insitam; est usus legentis in iis Nam liber tempor cum soluta nobis eleifend option congue nihil imperdiet doming id quod mazim placerat facer possim assum. Typi non habent claritatem insitam; est usus leg</p>

  <section class="brand-grid">
    <article class="brand-card"><h2>BRAND NAME</h2><div class="card-body"><div class="card-top"><div class="brand-image" role="img" aria-label="Brand product image"></div><p>delenit augue duis dolore te feugait nulla facilisi. Nam liber tempor cum soluta usv soluta us</p></div><p class="card-text">delenit augue duis dolore te feugait nulla facilisi. Nam liber tempor cum soluta nobis eleifend option congue nihil imperdiet doming id quod mazim placerat facer possim assum. Typi non habusv</p></div></article>
    <article class="brand-card"><h2>BRAND NAME</h2><div class="card-body"><div class="card-top"><div class="brand-image" role="img" aria-label="Brand product image"></div><p>delenit augue duis dolore te feugait nulla facilisi. Nam liber tempor cum soluta usv soluta us</p></div><p class="card-text">delenit augue duis dolore te feugait nulla facilisi. Nam liber tempor cum soluta nobis eleifend option congue nihil imperdiet doming id quod mazim placerat facer possim assum. Typi non habusv</p></div></article>
    <article class="brand-card"><h2>BRAND NAME</h2><div class="card-body"><div class="card-top"><div class="brand-image" role="img" aria-label="Brand product image"></div><p>delenit augue duis dolore te feugait nulla facilisi. Nam liber tempor cum soluta usv soluta us</p></div><p class="card-text">delenit augue duis dolore te feugait nulla facilisi. Nam liber tempor cum soluta nobis eleifend option congue nihil imperdiet doming id quod mazim placerat facer possim assum. Typi non habusv</p></div></article>
    <article class="brand-card"><h2>BRAND NAME</h2><div class="card-body"><div class="card-top"><div class="brand-image" role="img" aria-label="Brand product image"></div><p>delenit augue duis dolore te feugait nulla facilisi. Nam liber tempor cum soluta usv soluta us</p></div><p class="card-text">delenit augue duis dolore te feugait nulla facilisi. Nam liber tempor cum soluta nobis eleifend option congue nihil imperdiet doming id quod mazim placerat facer possim assum. Typi non habusv</p></div></article>
    <article class="brand-card"><h2>BRAND NAME</h2><div class="card-body"><div class="card-top"><div class="brand-image" role="img" aria-label="Brand product image"></div><p>delenit augue duis dolore te feugait nulla facilisi. Nam liber tempor cum soluta usv soluta us</p></div><p class="card-text">delenit augue duis dolore te feugait nulla facilisi. Nam liber tempor cum soluta nobis eleifend option congue nihil imperdiet doming id quod mazim placerat facer possim assum. Typi non habusv</p></div></article>
    <article class="brand-card"><h2>BRAND NAME</h2><div class="card-body"><div class="card-top"><div class="brand-image" role="img" aria-label="Brand product image"></div><p>delenit augue duis dolore te feugait nulla facilisi. Nam liber tempor cum soluta usv soluta us</p></div><p class="card-text">delenit augue duis dolore te feugait nulla facilisi. Nam liber tempor cum soluta nobis eleifend option congue nihil imperdiet doming id quod mazim placerat facer possim assum. Typi non habusv</p></div></article>
  </section>

  <footer class="site-footer">
    <div class="footer-col" style="left:15px"><h3>ABOUT US</h3><ul><li>Meridian</li><li>advertising</li><li>and Printing LTD.</li></ul></div>
    <div class="footer-col" style="left:134px"><h3>ADVERTISING</h3><ul><li>Roff Lorum</li><li>Texture Ipsum</li><li>Kinder Lines</li><li>Way Wing Lin</li></ul></div>
    <div class="footer-col" style="left:261px"><h3>DISPLAY</h3><ul><li>Paper Lalpic</li><li>Texture Surface</li><li>Dotted Lines</li><li>Dinamic piece</li></ul></div>
    <div class="footer-col" style="left:389px"><h3>PRINTING</h3><ul><li>Ligh Sink Ink</li><li>Ringer Ink</li><li>Roller Mask</li><li>Pinger Nash</li></ul></div>
    <div class="footer-col" style="left:515px"><h3>BRAND</h3><ul><li>Ringer Ink</li><li>X Printing</li><li>Cool Paper</li><li>Texture Diamond</li></ul></div>
    <div class="footer-col" style="left:643px"><h3>CONTACT US</h3><ul><li>555-010-2233</li><li>admin@meridianadv.com</li></ul></div>
  </footer>
  <div class="footer-bar">© Copyright 2012 Meridian Advertising and Printing LTD.
    <div class="social" aria-label="Social links"><span></span><span></span></div>
  </div>
</div>
</body>
</html>
```